Postcard Mailer to upscale luxury homeowners

We are a new company in the Tucson AZ market and want to use postcard marketing in key target markets. We clean and seal natural stone - granite, travertine, slate, etc. See website - http://www.brightvaultcoatings.example/ for more information about about our services and before/after photos in our "gallery" section.The logo from the site - Bright Vault Coatings - needs to be on the post card. The before/after photos from the photo "gallery" on the site demonstrate what can be done. We think a promo of $XXX off to any one requesting an estimate and presenting the postcard is worth trying. We have additional photos and information if needed.

Target Market(s)

Upscale residential homes in luxury home subdivisions

Industry/Entity Type

Home Improvement

Font styles to use
Sans Serif
Script

Requirements
Must have
• Logo
• Before/After photo (see website gallery for potential photos)
• website
• contact
• life time guarantee
• Feel of richness
Nice to have
• A call to action. $XXX dollar discount when estimate scheduled within/by ZZ
Should not have
• Won't know until I see it

```html
<!DOCTYPE html>
<html lang="en">
<head>
<meta charset="utf-8">
<title>Bright Vault Coatings – Postcard Mailer</title>
<link rel="stylesheet" href="https://fonts.googleapis.com/css2?family=Oswald:wght@400;500;600&family=Lato:wght@400;700&display=swap">
<style>
  :root {
    --stage: #5e5e5e;
    --navy: #1b4d6b;
    --olive: #a8a87a;
    --white: #ffffff;
    --sky: #7fc4e2;
    --slot: #e5e5e5;
  }
  * { margin: 0; padding: 0; box-sizing: border-box; }
  html, body { width: 900px; height: 1200px; overflow: hidden; }
  body { background: var(--stage); position: relative; font-family: "Lato", sans-serif; }

  .postcard {
    position: absolute; left: 52px; width: 796px; height: 514px;
    overflow: hidden; background: var(--white);
  }
  .postcard--front { top: 64px; }
  .postcard--back { top: 614px; }
  .postcard svg { position: absolute; inset: 0; width: 796px; height: 514px; display: block; }

  /* front */
  .brand {
    position: absolute; left: 505px; top: 48px;
    display: flex; align-items: center; gap: 10px;
  }
  .brand__dot { width: 22px; height: 22px; border-radius: 50%; background: var(--white); flex: none; }
  .brand__name {
    font-family: "Oswald", sans-serif; font-weight: 500; font-size: 24px;
    color: var(--white); letter-spacing: 1px; text-transform: uppercase; line-height: 1.1;
  }
  .brand__guarantee {
    position: absolute; left: 537px; top: 84px;
    font-family: "Oswald", sans-serif; font-weight: 500; font-size: 15px;
    color: var(--olive); letter-spacing: 2px; text-transform: uppercase;
  }
  .offer {
    position: absolute; left: 51px; top: 328px; width: 337px; height: 186px;
    background: var(--navy); border-radius: 18px 18px 0 0;
    text-align: center; padding-top: 32px;
    font-family: "Oswald", sans-serif; text-transform: uppercase;
  }
  .offer__amount { font-size: 31px; font-weight: 500; color: var(--white); line-height: 1.1; }
  .offer__condition { font-size: 21px; font-weight: 500; color: var(--white); letter-spacing: .5px; line-height: 1.25; }
  .offer__deadline { font-size: 47px; font-weight: 600; color: var(--olive); letter-spacing: 1px; line-height: 1.1; }

  /* back */
  .contact { position: absolute; left: 36px; top: 262px; }
  .contact__cta {
    font-family: "Oswald", sans-serif; font-weight: 500; font-size: 25px;
    color: var(--olive); text-transform: uppercase; letter-spacing: .5px;
  }
  .contact__phone {
    font-family: "Oswald", sans-serif; font-weight: 500; font-size: 70px;
    color: var(--white); line-height: 1; letter-spacing: -1px;
  }
  .contact__area {
    font-size: 14px; color: var(--sky); text-transform: uppercase; margin-top: 4px; letter-spacing: .3px;
  }
  .address {
    position: absolute; left: 0; top: 427px; width: 360px; height: 55px;
    background: var(--olive); border-radius: 0 28px 28px 0;
    padding: 9px 0 0 36px; color: var(--white);
    font-size: 14px; line-height: 1.4; text-transform: uppercase;
  }
  .website {
    position: absolute; left: 36px; top: 489px;
    font-size: 13px; color: var(--white); letter-spacing: .3px;
  }
</style>
</head>
<body>

<section class="postcard postcard--front">
  <svg viewBox="0 0 796 514">
    <defs>
      <clipPath id="front-photo-area">
        <path d="M0,58 C150,38 300,58 420,108 C530,155 640,205 796,185 V440 C640,470 470,420 300,400 C180,386 80,400 0,420 Z"/>
      </clipPath>
      <linearGradient id="kitchen-tone" x1="0" y1="0" x2="0" y2="1">
        <stop offset="0" stop-color="#ecebea"/><stop offset=".6" stop-color="#d6d2cc"/><stop offset="1" stop-color="#9a8f83"/>
      </linearGradient>
      <linearGradient id="tile-tone" x1="0" y1="0" x2="1" y2="1">
        <stop offset="0" stop-color="#7d6a57"/><stop offset=".5" stop-color="#8e7762"/><stop offset="1" stop-color="#6a5848"/>
      </linearGradient>
      <linearGradient id="hall-tone" x1="0" y1="0" x2="0" y2="1">
        <stop offset="0" stop-color="#d9d3c6"/><stop offset="1" stop-color="#c9b99c"/>
      </linearGradient>
    </defs>
    <rect width="796" height="514" fill="var(--navy)"/>
    <path d="M0,40 C150,20 300,40 420,90 C530,137 640,187 796,167 V514 H0 Z" fill="var(--white)"/>
    <path d="M0,430 C80,410 180,396 300,410 C470,430 640,480 796,450 V514 H0 Z" fill="var(--olive)"/>
    <g clip-path="url(#front-photo-area)">
      <rect x="0" y="0" width="226" height="514" fill="url(#kitchen-tone)" role="img" aria-label="Photo: modern kitchen with a polished granite countertop"/>
      <rect x="226" y="0" width="294" height="514" fill="url(#tile-tone)" role="img" aria-label="Photo: shower wall clad in natural stone tile"/>
      <rect x="520" y="0" width="276" height="514" fill="url(#hall-tone)" role="img" aria-label="Photo: hallway with sealed travertine floor and stacked stone wall"/>
    </g>
  </svg>
  <div class="brand">
    <span class="brand__dot"></span>
    <span class="brand__name">Bright Vault Coatings</span>
  </div>
  <p class="brand__guarantee">Lifetime Guarantee</p>
  <div class="offer">
    <p class="offer__amount">$XXX Dollar Discount</p>
    <p class="offer__condition">When Estimate Scheduled</p>
    <p class="offer__deadline">Within/By ZZ</p>
  </div>
</section>

<section class="postcard postcard--back">
  <svg viewBox="0 0 796 514">
    <defs>
      <linearGradient id="dining-tone" x1="0" y1="0" x2="1" y2="1">
        <stop offset="0" stop-color="#b9b3a8"/><stop offset=".5" stop-color="#6e4a38"/><stop offset="1" stop-color="#5d605f"/>
      </linearGradient>
    </defs>
    <path d="M0,0 H458 C500,70 520,150 500,260 C485,360 450,440 440,514 H0 Z" fill="var(--olive)"/>
    <path d="M0,0 H440 C480,70 498,150 480,260 C465,360 432,440 420,514 H0 Z" fill="var(--navy)"/>
    <path d="M0,220 C140,188 330,208 430,172 C470,140 470,60 440,0 H0 Z" fill="var(--olive)"/>
    <path d="M0,204 C140,172 320,192 415,158 C452,128 452,60 425,0 H0 Z" fill="url(#dining-tone)" role="img" aria-label="Photo: dining room with slate tile floor and leather chairs"/>
    <rect x="668" y="16" width="114" height="117" fill="var(--slot)"/>
    <rect x="526" y="270" width="246" height="124" fill="var(--slot)"/>
  </svg>
  <div class="contact">
    <p class="contact__cta">Call Today! Free Estimates!</p>
    <p class="contact__phone">520.555.0148</p>
    <p class="contact__area">Serving Tucson and surrounding areas</p>
  </div>
  <div class="address">
    <p>1180 W Palo Verde Rd., Suite 210</p>
    <p>Tucson, AZ 85741</p>
  </div>
  <p class="website">www.brightvaultcoatings.example</p>
</section>

</body>
</html>
```